Corvane Holdings , new business card design

investment firm with corporate clients . need double sided business card , vertical and horizontal options ,logo must be clear. prefer pantone colors only and sharp design. website also www.corvane-demo.ae

Khalid Bin Rashed
Managing Director
Tel. +971 4 000 1234
Mobile +971 50 000 5678
khalid@corvane-demo.ae
Palmgate Tower, officw 18-B07, Noor Terraces, Dubai

Khalid Bin Rashed
Managing Director

Serif

Designer to choose colors to be used in the design.

```html
<!DOCTYPE html>
<html lang="en">
<head>
<meta charset="utf-8">
<title>Corvane Holdings — Business Card</title>
<link rel="stylesheet" href="https://fonts.googleapis.com/css2?family=Fenix&display=swap">
<style>
  :root {
    --backdrop: #e7e4df;
    --card: #ffffff;
    --ink: #16171c;
    --accent: #4a6c98;
    --rule: #8a8a8a;
    --band: #0b0d17;
    --band-text: #f2f2f2;
  }
  * { margin: 0; padding: 0; box-sizing: border-box; }
  html, body {
    width: 900px; height: 1200px; overflow: hidden;
    background: var(--backdrop);
    font-family: "Fenix", Georgia, serif;
    color: var(--ink);
  }
  .card {
    position: absolute; left: 80px; width: 740px; height: 433px;
    background: radial-gradient(ellipse at 55% 60%, #ffffff 0%, #f7f7f7 70%, #f1f1f1 100%);
    box-shadow: 0 2px 8px rgba(0,0,0,0.25);
    overflow: hidden;
  }
  .card--front { top: 140px; }
  .card--back { top: 631px; height: 432px; }

  .holder {
    position: absolute; top: 98px; left: 0; width: 100%;
    text-align: center;
  }
  .holder__name { font-size: 30px; line-height: 40px; font-weight: 400; letter-spacing: 0.2px; }
  .holder__title { font-size: 19px; line-height: 24px; color: var(--accent); }

  .divider {
    position: absolute; top: 267px; left: 58px; width: 626px; height: 1px;
    background: var(--rule);
  }

  .contact { position: absolute; top: 280px; left: 58px; list-style: none; }
  .contact__item {
    display: flex; align-items: center; height: 23px;
    font-size: 15.5px; letter-spacing: 0.2px;
  }
  .contact__icon { width: 21px; height: 21px; margin-right: 10px; flex: none; }

  .address {
    position: absolute; top: 280px; right: 56px;
    text-align: right; font-size: 15.5px; line-height: 23px; letter-spacing: 0.2px;
    font-style: normal;
  }

  .web-band {
    position: absolute; left: 0; bottom: 0; width: 100%; height: 35px;
    background: var(--band); color: var(--band-text);
    display: flex; align-items: center; justify-content: center;
    font-size: 15px; letter-spacing: 6px; text-transform: uppercase;
  }

  .wordmark {
    position: absolute; top: 208px; left: 0; width: 100%;
    text-align: center; line-height: 44px;
    font-size: 36px; letter-spacing: 11px; text-transform: uppercase;
    color: var(--ink); padding-left: 11px;
  }
</style>
</head>
<body>

<section class="card card--front" aria-label="Business card front">
  <div class="holder">
    <h1 class="holder__name">Khalid Bin Rashed</h1>
    <p class="holder__title">Managing Director</p>
  </div>

  <div class="divider"></div>

  <ul class="contact">
    <li class="contact__item">
      <svg class="contact__icon" viewBox="0 0 22 22" aria-hidden="true">
        <circle cx="11" cy="11" r="9.8" fill="none" stroke="var(--accent)" stroke-width="1.4"/>
        <path d="M6.5 10.2c0-1.6 2-2.6 4.5-2.6s4.5 1 4.5 2.6l-1.8.5-.4-1.3c-1.5-.4-3-.4-4.6 0l-.4 1.3z" fill="var(--accent)"/>
        <path d="M8.3 11.2h5.4l1 3.3H7.3z" fill="var(--accent)"/>
      </svg>
      <span>+971 4 000 1234</span>
    </li>
    <li class="contact__item">
      <svg class="contact__icon" viewBox="0 0 22 22" aria-hidden="true">
        <circle cx="11" cy="11" r="9.8" fill="none" stroke="var(--accent)" stroke-width="1.4"/>
        <rect x="8" y="5.5" width="6" height="11" rx="1" fill="none" stroke="var(--accent)" stroke-width="1.3"/>
        <rect x="9.2" y="7" width="3.6" height="4.5" fill="var(--accent)"/>
      </svg>
      <span>+971 50 000 5678</span>
    </li>
    <li class="contact__item">
      <svg class="contact__icon" viewBox="0 0 22 22" aria-hidden="true">
        <circle cx="11" cy="11" r="9.8" fill="none" stroke="var(--accent)" stroke-width="1.4"/>
        <rect x="6" y="7.5" width="10" height="7" fill="var(--accent)"/>
        <path d="M6 7.8l5 3.8 5-3.8" fill="none" stroke="#ffffff" stroke-width="1"/>
      </svg>
      <span>khalid@corvane-demo.ae</span>
    </li>
  </ul>

  <address class="address">
    Palmgate Tower<br>
    office 18-B07, Noor Terraces, Dubai
  </address>

  <div class="web-band">www.corvane-demo.ae</div>
</section>

<section class="card card--back" aria-label="Business card back">
  <p class="wordmark">Corvane Holdings</p>
</section>

</body>
</html>
```